Harbinger Noble Alloys Works Business Cards

We are wanting to have a new business card designed for our company as we go to a convention. We want to balance business/Modern with elegance and beauty. Our company sells highend jewelry pieces. We want to utilize the colors of Black and Gold and have gold foiled fonts to be physically printed on the business cards.
We also would like to have space to write notes on the back side of the business card. When we meet people at jewelry conventions we would like to write notes if possible.
Here are websites and designs that we like the look and feel of these companies and you can use these as design ideas.
https://www.lorvanne.com
https://www.bellquist.com/en-us/home
Here is our company website link
www.harbingernaw.com
I also up loaded two versions of our logo.
- Update 4.26.22
I have uploaded photos of a business card we like. this card has raised embossed letters that you can feel. the raise letters are like a plastic but we don't need to use that...I uploaded to show you that we like the experience of the client feeling the characters of the logo. we also would like to have the material as a satin or some material very soft.
- Maybe we can get designs with beautiful gold foiling and raised characters and logos. we like simplicity...not busy but an elegant design. We need to write notes and would like a section where we can write notes. but we want an elegant style and the client has an experience with the feel of the card when they touch the card.
Colors
- Main colors Black & Gold
- white or light colors for small notes section.
Specialty ideals and things we would like to see based on your design styles.
- raised fonts
- raised logos
- gold foiling
- satin/soft finish on the card material.
we are wanting to design a business card that looks elegant and clean. When the client is handed the business card we want them to physically experience the business card as well by touching the raised logos or fonts and the base material is soft satin. I hope this helps with further designs.
thank you all
We uploaded a new contact layout that we have designed in our office. we would like to see how this would look on your designs.
thank you
I just finished uploading the Contact Layout. the colors are just examples. please use this layout as an idea and use colors based on the feed back we have given each of you personally.
Contact Information for Business Card
we need an area to write notes, we would like to have our logos or the diamond of our logo or the business card to have embossed sections to the business card so when the customer touches the card they can feel the logo. we would also like sections of our business card to have gold foiling. we would also like to use a satin soft paper with our card. when the client touches the card its super soft and high quality
Requirements
Must have
- we would like to have our logos or the diamond of our logo or the business card to have embossed sections to the business card so when the customer touches the card they can feel the logo. we would also like sections of our business card to have gold foiling. we would also like to use a satin soft paper with our card. when the client touches the card its super soft and high quality
Nice to have
- we would like to have our logos or the diamond of our logo or the business card to have embossed sections to the business card so when the customer touches the card they can feel the logo. we would also like sections of our business card to have gold foiling.

```html
<!DOCTYPE html>
<html lang="en">
<head>
<meta charset="utf-8">
<title>Harbinger Noble Alloys – Business Cards</title>
<link rel="stylesheet" href="https://fonts.googleapis.com/css2?family=Cinzel:wght@500&family=Open+Sans:wght@400&display=swap">
<style>
  :root {
    --canvas: #d6d6d6;
    --card-black: #050505;
    --card-charcoal: #1e1e1e;
    --gold: #c9a437;
    --white: #f2f2f2;
    --notes-band: #dcdcdc;
    --divider: #bdbdbd;
  }
  * { margin: 0; padding: 0; box-sizing: border-box; }
  html, body { width: 1156px; height: 1200px; overflow: hidden; }
  body {
    background: var(--canvas);
    display: flex;
    flex-direction: column;
    align-items: center;
    justify-content: center;
    gap: 56px;
  }
  .card {
    position: relative;
    width: 900px;
    height: 514px;
    border-radius: 36px;
    overflow: hidden;
    box-shadow: 0 6px 10px rgba(0,0,0,0.35);
  }
  .brand {
    position: absolute;
    left: 0; right: 0;
    text-align: center;
    font-family: "Cinzel", serif;
    font-weight: 500;
    color: var(--gold);
  }
  .brand-name { display: block; letter-spacing: 0.5px; }
  .brand-tagline { display: block; }

  /* Contact side */
  .card-front {
    background: linear-gradient(100deg, var(--card-black) 0%, var(--card-black) 45%, var(--card-charcoal) 100%);
  }
  .card-front .brand { top: 100px; }
  .card-front .brand-name { font-size: 38px; line-height: 44px; }
  .card-front .brand-tagline { font-size: 28px; line-height: 34px; }
  .notes-band {
    position: absolute;
    left: 0; right: 0; bottom: 0;
    height: 104px;
    background: var(--notes-band);
  }
  .person {
    position: absolute;
    right: 510px;
    top: 268px;
    text-align: right;
    font-family: "Open Sans", sans-serif;
  }
  .person-name { color: var(--gold); font-size: 34px; line-height: 40px; }
  .person-role { color: var(--white); font-size: 22px; line-height: 28px; }
  .divider {
    position: absolute;
    left: 434px;
    top: 203px;
    width: 2px;
    height: 184px;
    background: var(--divider);
  }
  .contact {
    position: absolute;
    left: 464px;
    top: 200px;
    font-family: "Open Sans", sans-serif;
    font-size: 24px;
    line-height: 34px;
    color: var(--white);
    font-style: normal;
  }
  .contact-address { margin-bottom: 24px; }

  /* Brand side */
  .card-back { background: var(--card-black); }
  .pattern-field {
    position: absolute;
    inset: 0;
    background: radial-gradient(ellipse at 55% 45%, #2a2a2a 0%, #141414 55%, #070707 100%);
  }
  .card-back .brand { top: 218px; }
  .card-back .brand-name { font-size: 52px; line-height: 62px; }
  .card-back .brand-tagline { font-size: 40px; line-height: 48px; }
</style>
</head>
<body>

  <section class="card card-front" aria-label="Business card contact side">
    <div class="brand">
      <span class="brand-name">Harbinger Noble Alloys</span>
      <span class="brand-tagline">– Coins, Jewelry &amp; Diamonds –</span>
    </div>
    <div class="person">
      <p class="person-name">DANIEL REYES</p>
      <p class="person-role">Manager</p>
    </div>
    <div class="divider"></div>
    <address class="contact">
      <p class="contact-address">2740 Larkspur Ave NE,<br>Ashford, OR 97390</p>
      <p>(555)201-7734</p>
      <p>dan@harbingernaw.com</p>
      <p>www.harbingernaw.com</p>
    </address>
    <div class="notes-band" aria-label="Notes area"></div>
  </section>

  <section class="card card-back" aria-label="Business card brand side">
    <div class="pattern-field" role="img" aria-label="Embossed tonal gem pattern covering the card"></div>
    <div class="brand">
      <span class="brand-name">Harbinger Noble Alloys</span>
      <span class="brand-tagline">– Coins, Jewelry &amp; Diamonds –</span>
    </div>
  </section>

</body>
</html>
```